Text Box for making an update on our website

We need an awesome "Text Box" so that our Users can make an amazing Post or update on our website or App.

Let's make something super duper like Pictavo, Friendloop, Chirr or Qmeld text box but a bit more amazing....

I've included our current desktop and Mobile "Text Box" which needs love :)

Our Text Box by default makes a Post "Private" the User can change it to "Public"

I have included what a final "Post" looks like on our site.

Could we incorporate a bit of the "Post" design into the "Create Post" design..... maybe make the header similar.

thanks

Morgan

Target Market(s)

Health Care, Hospitals, Caregivers, Nurses

Industry/Entity Type

Health Care

Font styles to use
Other font styles liked:
• Comfortaa

Requirements
Must have
• Our main colors are

#1D44B8 - Blue
#D85097 - Pink
Nice to have
• Super clean and simple. Happy and Easy to use
Should not have
• Complicated

Too many colors

```html
<!DOCTYPE html>
<html lang="en">
<head>
<meta charset="utf-8">
<title>Create Post</title>
<link href="https://fonts.googleapis.com/css2?family=Poppins:wght@300;400&display=swap" rel="stylesheet">
<style>
  :root {
    --blue: #244cbc;
    --pink: #d85097;
    --white: #ffffff;
    --ink: #2a2a2a;
    --stage: #b9b9b9;
    --rule: #bdbdbd;
    --hint-blue: #8c9de0;
    --hint-pink: #eba6ca;
  }
  * { box-sizing: border-box; margin: 0; padding: 0; }
  html, body { width: 1200px; height: 1200px; overflow: hidden; }
  body {
    background: var(--stage);
    font-family: "Poppins", sans-serif;
    position: relative;
  }
  .composer {
    position: absolute;
    left: 92px;
    width: 1015px;
    height: 327px;
    background: var(--white);
    border-radius: 32px;
    overflow: hidden;
    box-shadow: 0 6px 10px rgba(0,0,0,0.18);
  }
  .composer--public { top: 275px; --band: var(--pink); --button: var(--blue); --hint: var(--hint-blue); }
  .composer--private { top: 669px; --band: var(--blue); --button: var(--pink); --hint: var(--hint-pink); }

  .composer__title {
    position: absolute; left: 59px; top: 25px;
    font-size: 33px; font-weight: 400; color: var(--ink); line-height: 1;
  }
  .composer__divider {
    position: absolute; left: 0; right: 0; top: 89px; height: 2px; background: var(--rule);
  }
  .composer__close { position: absolute; left: 956px; top: 31px; width: 28px; height: 28px; }

  .privacy-toggle {
    position: absolute; top: 20px; width: 180px; height: 50px; border-radius: 25px;
    color: var(--white); font-size: 23px; font-weight: 300; line-height: 50px;
  }
  .composer--public .privacy-toggle { left: 715px; background: var(--blue); }
  .composer--private .privacy-toggle { left: 709px; background: var(--pink); }
  .privacy-toggle__label { position: absolute; top: 0; }
  .composer--public .privacy-toggle__label { right: 32px; }
  .composer--private .privacy-toggle__label { left: 34px; }
  .privacy-toggle__knob {
    position: absolute; top: -3px; width: 56px; height: 56px; border-radius: 50%;
    border: 4px solid var(--white);
  }
  .composer--public .privacy-toggle__knob { left: -2px; background: var(--blue); }
  .composer--private .privacy-toggle__knob { right: -2px; background: var(--pink); }
  .privacy-toggle__knob svg { width: 100%; height: 100%; display: block; }

  .composer__cursor {
    position: absolute; left: 60px; top: 115px; width: 3px; height: 39px; background: var(--button);
  }
  .composer__placeholder {
    position: absolute; left: 67px; top: 116px; font-size: 30px; font-weight: 300;
    color: var(--hint); line-height: 1.2;
  }

  .composer__band {
    position: absolute; left: 0; right: 0; top: 233px; bottom: 0; background: var(--band);
  }
  .composer__band::before {
    content: ""; position: absolute; left: 0; right: 0; top: -1px; height: 2px; background: var(--rule); opacity: 0.6;
  }

  .action { position: absolute; top: 191px; width: 150px; margin-left: -75px; text-align: center; }
  .action__icon {
    width: 86px; height: 86px; margin: 0 auto; border-radius: 50%;
    background: var(--button); border: 3px solid var(--band);
    display: flex; align-items: center; justify-content: center;
  }
  .action__icon svg { width: 48px; height: 48px; }
  .action__label {
    display: block; margin-top: 7px; color: var(--white); font-size: 21px; font-weight: 300; white-space: nowrap;
  }
  .action--photos { left: 104px; }
  .action--checkin { left: 259px; }
  .action--tag { left: 414px; }
  .action--tag .action__label, .action--emoji .action__label { margin-top: 4px; }
  .action--emoji { left: 569px; }
  .action--files { left: 723px; }

  .composer__send {
    position: absolute; left: 869px; top: 182px; width: 98px; height: 98px; border-radius: 50%;
    background: var(--white); border: 4px solid var(--button);
    display: flex; align-items: center; justify-content: center;
  }
  .composer__send svg { width: 60px; height: 60px; }

  .icon-line { fill: none; stroke: var(--white); stroke-width: 2.4; stroke-linecap: round; stroke-linejoin: round; }
</style>
</head>
<body>

<svg width="0" height="0" style="position:absolute">
  <defs>
    <symbol id="icon-photos" viewBox="0 0 48 48">
      <rect class="icon-line" x="12" y="7" width="30" height="24" rx="3"/>
      <rect class="icon-line" x="9" y="10" width="30" height="24" rx="3" fill="var(--button)"/>
      <rect class="icon-line" x="5" y="14" width="30" height="26" rx="3" fill="var(--button)"/>
      <circle class="icon-line" cx="21" cy="23" r="3"/>
      <path class="icon-line" d="M5 36 L14 27 L22 33 L27 29 L35 35"/>
    </symbol>
    <symbol id="icon-pin" viewBox="0 0 48 48">
      <path class="icon-line" d="M24 4 C15 4 9 10 9 18 C9 27 19 33 24 40 C29 33 39 27 39 18 C39 10 33 4 24 4 Z"/>
      <circle class="icon-line" cx="24" cy="18" r="9"/>
      <path class="icon-line" d="M24 22 L20 18.5 A2.2 2.2 0 0 1 24 16 A2.2 2.2 0 0 1 28 18.5 Z" stroke-width="1.8"/>
      <path class="icon-line" d="M24 40 L24 45 M17 45 L31 45"/>
    </symbol>
    <symbol id="icon-tag" viewBox="0 0 48 48">
      <path class="icon-line" d="M26 8 L40 8 L40 22 L18 44 L4 30 Z"/>
      <path class="icon-line" d="M27 11 L37 11 L37 21 L18 40 L8 30 Z" stroke-width="1.2" stroke-dasharray="1.5 2"/>
      <circle class="icon-line" cx="33" cy="15" r="2.6"/>
      <path class="icon-line" d="M34 14 L44 3"/>
    </symbol>
    <symbol id="icon-smile" viewBox="0 0 48 48">
      <circle class="icon-line" cx="24" cy="24" r="20"/>
      <circle cx="17" cy="19" r="2.4" fill="var(--white)"/>
      <circle cx="31" cy="19" r="2.4" fill="var(--white)"/>
      <path class="icon-line" d="M14 26 C16 36 32 36 34 26"/>
    </symbol>
    <symbol id="icon-clip" viewBox="0 0 48 48">
      <path class="icon-line" d="M30 14 L14 32 C11 36 15 41 19 38 L38 17 C43 11 36 3 30 9 L10 31 C4 38 12 47 19 41 L34 25"/>
    </symbol>
  </defs>
</svg>

<section class="composer composer--public" aria-label="Create post, public">
  <h1 class="composer__title">Creat Post</h1>
  <div class="privacy-toggle">
    <span class="privacy-toggle__knob">
      <svg viewBox="0 0 56 56"><g stroke="var(--pink)" stroke-width="2.6" stroke-linecap="round">
        <path d="M24 14 V21 M24 27 V34 M14 24 H21 M27 24 H34 M17 17 L21 21 M27 27 L31 31 M31 17 L27 21 M21 27 L17 31" transform="translate(4 4)"/>
      </g></svg>
    </span>
    <span class="privacy-toggle__label">Public</span>
  </div>
  <svg class="composer__close" viewBox="0 0 28 28"><path d="M3 3 L25 25 M25 3 L3 25" stroke="var(--ink)" stroke-width="2.4"/></svg>
  <div class="composer__divider"></div>
  <div class="composer__cursor"></div>
  <p class="composer__placeholder">Share A New Post</p>
  <div class="composer__band"></div>
  <div class="action action--photos"><div class="action__icon"><svg><use href="#icon-photos"/></svg></div><span class="action__label">Add Photos</span></div>
  <div class="action action--checkin"><div class="action__icon"><svg><use href="#icon-pin"/></svg></div><span class="action__label">Check-in</span></div>
  <div class="action action--tag"><div class="action__icon"><svg><use href="#icon-tag"/></svg></div><span class="action__label">Tag Friends</span></div>
  <div class="action action--emoji"><div class="action__icon"><svg><use href="#icon-smile"/></svg></div><span class="action__label">Emoji</span></div>
  <div class="action action--files"><div class="action__icon"><svg><use href="#icon-clip"/></svg></div><span class="action__label">Add Files</span></div>
  <div class="composer__send" aria-label="Send">
    <svg viewBox="0 0 60 60"><path d="M6 24 L54 6 L36 54 L31 29 Z" fill="var(--pink)"/><path d="M31 29 L54 6" stroke="var(--white)" stroke-width="2"/></svg>
  </div>
</section>

<section class="composer composer--private" aria-label="Create post, private">
  <h1 class="composer__title">Creat Post</h1>
  <div class="privacy-toggle">
    <span class="privacy-toggle__label">Private</span>
    <span class="privacy-toggle__knob">
      <svg viewBox="0 0 56 56"><g stroke="var(--blue)" stroke-width="2.6" stroke-linecap="round">
        <path d="M24 14 V21 M24 27 V34 M14 24 H21 M27 24 H34 M17 17 L21 21 M27 27 L31 31 M31 17 L27 21 M21 27 L17 31" transform="translate(4 4)"/>
      </g></svg>
    </span>
  </div>
  <svg class="composer__close" viewBox="0 0 28 28"><path d="M3 3 L25 25 M25 3 L3 25" stroke="var(--ink)" stroke-width="2.4"/></svg>
  <div class="composer__divider"></div>
  <div class="composer__cursor"></div>
  <p class="composer__placeholder">Share A New Post</p>
  <div class="composer__band"></div>
  <div class="action action--photos"><div class="action__icon"><svg><use href="#icon-photos"/></svg></div><span class="action__label">Add Photos</span></div>
  <div class="action action--checkin"><div class="action__icon"><svg><use href="#icon-pin"/></svg></div><span class="action__label">Check-in</span></div>
  <div class="action action--tag"><div class="action__icon"><svg><use href="#icon-tag"/></svg></div><span class="action__label">Tag Friends</span></div>
  <div class="action action--emoji"><div class="action__icon"><svg><use href="#icon-smile"/></svg></div><span class="action__label">Emoji</span></div>
  <div class="action action--files"><div class="action__icon"><svg><use href="#icon-clip"/></svg></div><span class="action__label">Add Files</span></div>
  <div class="composer__send" aria-label="Send">
    <svg viewBox="0 0 60 60"><path d="M6 24 L54 6 L36 54 L31 29 Z" fill="var(--blue)"/><path d="M31 29 L54 6" stroke="var(--white)" stroke-width="2"/></svg>
  </div>
</section>

</body>
</html>
```